Heating and Cooling Company mobile website

We need a website specifically designed for a viewing on a mobile device.

We serve the northern New Jersey heating, cooling and electrical residential market.

The goal is the drive traffic to the site by using Brindle Pay Per click. People will be searching for an HVAC contractor, and they land on our page. They need to get key info quickly without all the clutter of a desktop type of site.

Target Market(s)

Homeowners

Industry/Entity Type

Hvac

Coding

Coded - Design and coding required

Number of Pages Required

5+ page

Font styles to use
Serif

Requirements
Must have
• View attachments to see samples of the desktop version. It must have a similar color scheme
• The copy of the website is also attached
Nice to have
• Would like it to have a sort of Quello feel to it. Make it seem like its an app that people are using and that its exciting to be on the website. It would be nice to have a page where customers can book appointments

```html
<!DOCTYPE html>
<html lang="en">
<head>
<meta charset="utf-8">
<title>Hearthline Climate – Mobile Home</title>
<link rel="stylesheet" href="https://fonts.googleapis.com/css2?family=Cormorant+Garamond:wght@600;700&family=Lato:wght@400;700;900&display=swap">
<style>
:root{
  --ink:#231f20;
  --beige:#ebe3cf;
  --sepia:#c9b89a;
  --navy:#232b4a;
  --red:#8a1428;
  --red-dark:#5e1220;
  --gold:#f0a84a;
  --orange:#ee7d2a;
  --cream:#f6efdc;
  --white:#ffffff;
  --text:#2a2a2a;
  --serif:'Cormorant Garamond', Georgia, serif;
  --sans:'Lato', Arial, sans-serif;
}
*{box-sizing:border-box;margin:0;padding:0}
html,body{width:1200px;height:3879px;overflow:hidden;background:var(--white)}
body{font-family:var(--sans);color:var(--text);position:relative}
section,header,footer{position:relative;width:1200px;overflow:hidden}

/* Header */
.site-header{height:253px;background:var(--ink)}
.brand{position:absolute;left:70px;top:74px;display:flex;align-items:center;gap:18px}
.brand-mark{width:42px;height:42px;background:var(--gold);border-radius:50%}
.brand-name{font-family:var(--serif);font-weight:700;font-size:58px;line-height:1;color:var(--cream);width:270px}
.menu-toggle{position:absolute;right:66px;top:96px;width:90px;height:72px;display:flex;flex-direction:column;justify-content:space-between}
.menu-toggle span{display:block;height:16px;background:var(--white);border-radius:3px}

/* Hero */
.hero{height:493px;background:var(--beige)}
.hero-photo{position:absolute;left:360px;top:0;width:840px;height:430px;background:radial-gradient(ellipse at 50% 60%,#3a3434 0%,#6d6253 38%,rgba(235,227,207,0) 72%)}
.hero-title{position:absolute;left:40px;top:80px;width:370px;text-align:center;font-family:var(--serif);font-weight:700;font-size:46px;line-height:60px;color:var(--ink);white-space:nowrap;z-index:2}
.btn-learn{position:absolute;left:104px;top:310px;width:215px;height:92px;background:var(--red);border:4px solid var(--gold);border-radius:46px;color:var(--white);font-family:var(--serif);font-size:32px;font-weight:700;text-align:center;padding-top:12px;line-height:34px;z-index:2}
.btn-schedule{position:absolute;left:905px;top:215px;width:240px;height:114px;background:var(--red);border:4px solid var(--gold);color:var(--white);text-align:center;padding-top:12px}
.btn-schedule strong{display:block;font-family:var(--serif);font-size:40px;line-height:44px}
.btn-schedule small{display:block;font-size:18px;font-weight:900;letter-spacing:1px}

/* Services */
.services{height:922px;background:var(--white)}
.services-band{position:absolute;left:0;top:0}
.service{position:absolute;width:420px;text-align:center}
.service-badge{display:block;margin:0 auto}
.service-shadow{width:250px;height:26px;margin:-2px auto 0;border-radius:50%;background:radial-gradient(ellipse,#bdbdbd 0%,rgba(255,255,255,0) 70%)}
.service-label{font-weight:900;font-size:34px;letter-spacing:1px;color:var(--navy);margin-top:20px}
.s1{left:103px;top:50px}.s2{left:659px;top:50px}
.s3{left:103px;top:452px}.s4{left:659px;top:452px}

/* News */
.news{height:1084px;background:var(--beige)}
.news-photo{position:absolute;left:0;top:0;width:1200px;height:560px;background:linear-gradient(180deg,#b7a78a 0%,#d3c5a8 55%,var(--beige) 100%)}
.news-item{position:absolute;top:515px;width:480px}
.news-item.left{left:76px}.news-item.right{left:647px}
.news-date{font-family:var(--serif);font-weight:700;font-size:54px;color:var(--ink);line-height:60px}
.news-body{font-size:30px;line-height:46px;margin-top:20px;color:var(--ink)}
.news-more{display:block;margin-top:34px;font-size:30px;color:var(--red)}
.news-rule{position:absolute;left:76px;right:66px;top:1010px;height:3px;background:#d8ccb0}

/* Footer */
.site-footer{height:1127px;background:var(--red)}
.footer-strip{position:absolute;left:0;top:0;width:1200px;height:48px;background:var(--navy)}
.footer-left{position:absolute;left:0;top:48px;width:575px;bottom:0;background:var(--red-dark)}
.footer-brand{position:absolute;left:90px;top:0;width:410px;height:150px;background:var(--red);border:5px solid var(--gold);border-radius:24px;display:flex;align-items:center;justify-content:center;gap:14px}
.footer-brand .brand-mark{width:30px;height:30px}
.footer-brand .brand-name{width:auto;font-size:48px;text-align:center}
.footer-contact{position:absolute;left:0;width:575px;top:225px;text-align:center;font-size:27px;line-height:44px;color:var(--white);font-style:normal}
.footer-links{position:absolute;list-style:none;font-size:27px;line-height:45px;color:var(--white)}
.footer-links li::before{content:"> "}
.fl-main{left:167px;top:455px}
.fl-heat{left:167px;top:775px}
.stay{position:absolute;left:687px;width:353px;top:150px;text-align:center;font-family:var(--serif);font-weight:700;font-size:40px;color:var(--white)}
.social{position:absolute;left:687px;top:205px;width:353px;height:126px;background:var(--orange);border:4px solid var(--gold);display:flex;justify-content:center;align-items:center;gap:20px}
.social span{width:66px;height:66px;border-radius:50%;background:var(--white)}
.footer-col{position:absolute;left:721px}
.footer-col h4{font-size:27px;font-weight:900;color:var(--white);line-height:45px}
.footer-col ul{list-style:none;font-size:27px;line-height:45px;color:var(--white)}
.footer-col li::before{content:"> "}
.fc1{top:412px}.fc2{top:635px}.fc3{top:905px}
</style>
</head>
<body>

<header class="site-header">
  <div class="brand"><span class="brand-mark"></span><span class="brand-name">Hearthline Climate</span></div>
  <div class="menu-toggle" aria-label="Menu"><span></span><span></span><span></span></div>
</header>

<section class="hero">
  <div class="hero-photo" role="img" aria-label="Family photo behind a company service van"></div>
  <h1 class="hero-title">Most Trusted<br>Heating &amp; Cooling<br>Company</h1>
  <a class="btn-learn">Learn More<br>›</a>
  <a class="btn-schedule"><strong>Schedule</strong><small>A SERVICE!</small></a>
</section>

<section class="services">
  <svg class="services-band" width="1200" height="300" viewBox="0 0 1200 300" aria-hidden="true">
    <rect width="1200" height="300" fill="#ffffff"/>
    <path d="M0 10 Q300 -8 600 30 Q900 -8 1200 10 L1200 265 Q900 240 600 250 Q300 240 0 265 Z" fill="var(--navy)"/>
    <path d="M0 0 H1200 V10 Q900 -8 600 30 Q300 -8 0 10 Z" fill="var(--beige)"/>
  </svg>

  <div class="service s1">
    <svg class="service-badge" width="300" height="270" viewBox="0 0 300 270" aria-hidden="true">
      <rect x="20" y="10" width="260" height="240" rx="60" fill="var(--red)" stroke="var(--gold)" stroke-width="10"/>
      <circle cx="150" cy="130" r="40" fill="none" stroke="var(--cream)" stroke-width="12"/>
      <g stroke="var(--cream)" stroke-width="12" stroke-linecap="round">
        <line x1="150" y1="55" x2="150" y2="70"/><line x1="150" y1="190" x2="150" y2="205"/>
        <line x1="75" y1="130" x2="90" y2="130"/><line x1="210" y1="130" x2="225" y2="130"/>
        <line x1="97" y1="77" x2="107" y2="87"/><line x1="193" y1="173" x2="203" y2="183"/>
        <line x1="203" y1="77" x2="193" y2="87"/><line x1="107" y1="173" x2="97" y2="183"/>
      </g>
    </svg>
    <div class="service-shadow"></div>
    <div class="service-label">HEATING</div>
  </div>

  <div class="service s2">
    <svg class="service-badge" width="300" height="270" viewBox="0 0 300 270" aria-hidden="true">
      <rect x="20" y="10" width="260" height="240" rx="60" fill="var(--red)" stroke="var(--gold)" stroke-width="10"/>
      <g stroke="var(--cream)" stroke-width="12" stroke-linecap="round">
        <line x1="150" y1="60" x2="150" y2="200"/>
        <line x1="89" y1="95" x2="211" y2="165"/>
        <line x1="89" y1="165" x2="211" y2="95"/>
      </g>
    </svg>
    <div class="service-shadow"></div>
    <div class="service-label">AIR CONDITIONING</div>
  </div>

  <div class="service s3">
    <svg class="service-badge" width="300" height="270" viewBox="0 0 300 270" aria-hidden="true">
      <rect x="20" y="10" width="260" height="240" rx="60" fill="var(--red)" stroke="var(--gold)" stroke-width="10"/>
      <g stroke="var(--cream)" stroke-width="12" stroke-linecap="round" fill="none">
        <path d="M95 90 H205"/><path d="M95 130 H205"/><path d="M95 170 H205"/>
      </g>
    </svg>
    <div class="service-shadow"></div>
    <div class="service-label">OTHER SERVICES</div>
  </div>

  <div class="service s4">
    <svg class="service-badge" width="300" height="270" viewBox="0 0 300 270" aria-hidden="true">
      <rect x="20" y="10" width="260" height="240" rx="60" fill="var(--red)" stroke="var(--gold)" stroke-width="10"/>
      <path d="M90 135 L150 80 L210 135 V190 H90 Z" fill="var(--cream)"/>
      <rect x="135" y="150" width="30" height="40" fill="var(--red)"/>
    </svg>
    <div class="service-shadow"></div>
    <div class="service-label">WHO WE SERVICE</div>
  </div>
</section>

<section class="news">
  <div class="news-photo" role="img" aria-label="Sepia photo of a family walking on a beach"></div>
  <article class="news-item left">
    <h2 class="news-date">AUGUST 26</h2>
    <p class="news-body">Lorem Ipsum is simply dummy text of the printing and typesetting industry. Lorem Ipsum has been the industry's standard dummy text ever since the 1500s, when an unknown printer</p>
    <a class="news-more">Read More ...</a>
  </article>
  <article class="news-item right">
    <h2 class="news-date">JULY 15</h2>
    <p class="news-body">Lorem Ipsum is simply dummy text of the printing and typesetting industry. Lorem Ipsum has been the industry's standard dummy text ever since the 1500s, when an unknown printer</p>
    <a class="news-more">Read More ...</a>
  </article>
  <div class="news-rule"></div>
</section>

<footer class="site-footer">
  <div class="footer-strip"></div>
  <div class="footer-left"></div>
  <div class="footer-brand"><span class="brand-mark"></span><span class="brand-name">Hearthline Climate</span></div>
  <address class="footer-contact">
    24 Linden Court,<br>Maplebrook, NJ 07990<br>555.010.4477<br>info@hearthlineclimate.com
  </address>
  <ul class="footer-links fl-main">
    <li>Home</li><li>About</li><li>Services</li><li>Testimonials</li><li>Blog</li><li>Contact</li>
  </ul>
  <ul class="footer-links fl-heat">
    <li>Heating</li><li>New Installation</li><li>Repair &amp; Service</li><li>Heat Pumps</li><li>Boilers</li><li>Radiant Heat Systems</li>
  </ul>

  <div class="stay">Stay Connected</div>
  <div class="social" aria-label="Social links"><span></span><span></span><span></span></div>

  <div class="footer-col fc1">
    <h4>Air Conditioning</h4>
    <ul><li>New Installation</li><li>Repair &amp; Service</li><li>Ductless Systems</li></ul>
  </div>
  <div class="footer-col fc2">
    <h4>Other Services</h4>
    <ul><li>Indoor Air Quality</li><li>Thermostats &amp; Zoning</li><li>Generators</li><li>Products</li></ul>
  </div>
  <div class="footer-col fc3">
    <h4>Who We Service</h4>
    <ul><li>Residential &amp; Homeowners</li><li>Commercial Business</li></ul>
  </div>
</footer>

</body>
</html>
```